Business card design needed for rebranded top-end landscaping business

We need a new business card design, incorporating our logo (colours Green #8dc63f and Grey #8a8c8e) and also some options that include the colour dark navy (eg #000040) as our uniforms are navy with white and grey trim.

We are an innovative landscaping company that maintains high-end gardens for meticulous clients. We pride ourselves on our customer service, our professionalism, and our workmanship.

Our business name needs to be easily read and our branding needs to be bold and memorable, without screaming "tradesman"! We prefer clean lines over lots of fine detail.

The design MUST include:
- Business name ("Brambleton Gardenworks")
- Logo (file uploaded)
- Employee name
- Phone number
- Email address
- www.brambletongardenworks.com.au
- Facebook & Instagram logos
- The Turfcraft Guild logo (file uploaded) along with the word "Member"
- Licence "Lic. 618392K"

OPTIONAL inclusions:
- "Creating outdoor spaces for our community to be inspired, refreshed and re-energised"
- "Landscape Maintenance - Irrigation - Arboriculture" (dashes can be replaced with dots or other)
- "Fully qualified, licensed & insured"
- "Residential - Strata - Commercial - Real Estate" (dashes can be replaced with dots or other)

High-end professionals and retirees, real estate agents

Landscaping

See Project description

Sans Serif

Designer to choose colors to be used in the design.

• Must incorporate our logo, and colours Green #8dc63f and Grey #8a8c8e) from the logo, and the colour DARK NAVY (eg #000040).
• The design MUST include:
• - Business name ("Brambleton Gardenworks")
• - Logo (file uploaded)
• - Employee name
• - Phone number
• - Email address
• - www.brambletongardenworks.com.au
• - Facebook & Instagram logos
• - The Turfcraft Guild logo (file uploaded) along with the word "Member"
• - Licence "Lic. 618392K"
• OPTIONAL inclusions:
• - "Creating outdoor spaces for our community to be inspired, refreshed and re-energised"
• - "Landscape Maintenance - Irrigation - Arboriculture" (dashes can be replaced with dots or other)
• - "Fully qualified, licensed & insured"
• - "Residential - Strata - Commercial - Real Estate" (dashes can be replaced with dots or other)

```html
<!DOCTYPE html>
<html lang="en">
<head>
<meta charset="utf-8">
<title>Brambleton Gardenworks — Business Card</title>
<link href="https://fonts.googleapis.com/css2?family=Didact+Gothic&display=swap" rel="stylesheet">
<style>
  :root {
    --green: #8dc63f;
    --grey: #8a8c8e;
    --ink: #4a4c4e;
    --white: #ffffff;
    --paper: #f7f7f7;
    --backdrop: #e9e7e3;
  }
  * { box-sizing: border-box; margin: 0; padding: 0; }
  html, body { width: 1200px; height: 900px; overflow: hidden; }
  body {
    background: var(--backdrop);
    font-family: "Didact Gothic", "Century Gothic", sans-serif;
    display: flex;
    align-items: center;
    justify-content: center;
    gap: 40px;
  }
  .card {
    position: relative;
    width: 560px;
    height: 342px;
    overflow: hidden;
    box-shadow: 0 6px 18px rgba(0,0,0,0.15);
  }

  /* Front */
  .card-front { background: var(--paper); }
  .side-band {
    position: absolute; left: 0; top: 0; bottom: 0; width: 70px;
    background: var(--green);
  }
  .side-band-name {
    position: absolute; left: 50%; top: 50%;
    transform: translate(-50%, -50%) rotate(-90deg);
    white-space: nowrap;
    color: var(--white);
    font-size: 24px;
  }
  .front-brand {
    position: absolute; right: 24px; top: 20px;
    display: flex; flex-direction: column; align-items: center; gap: 6px;
  }
  .brand-dot {
    width: 34px; height: 34px; border-radius: 50%;
    background: var(--grey);
  }
  .front-brand .brand-name { color: var(--grey); font-size: 15px; }
  .person {
    position: absolute; left: 100px; top: 88px;
  }
  .person-name { color: var(--green); font-size: 52px; letter-spacing: 2px; line-height: 1; }
  .person-role { color: var(--grey); font-size: 24px; letter-spacing: 1.5px; margin: 6px 0 0 66px; }

  .contact-list, .social-list {
    position: absolute; list-style: none;
    border-left: 2px solid var(--grey);
    padding-left: 12px;
    display: flex; flex-direction: column; gap: 12px;
  }
  .contact-list { left: 96px; top: 200px; }
  .social-list { left: 378px; top: 186px; gap: 10px; }
  .contact-list li, .social-list li {
    display: flex; align-items: center; gap: 10px;
    color: var(--ink); font-size: 11px; white-space: nowrap;
  }
  .icon { width: 18px; height: 18px; flex: none; }
  .social-mark {
    width: 18px; height: 18px; flex: none;
    border: 1.5px solid var(--green); border-radius: 4px;
  }
  .guild-badge {
    width: 22px; height: 14px; flex: none; background: var(--grey); border-radius: 2px;
  }
  .licence { padding-left: 2px; }

  /* Back */
  .card-back { background: var(--green); color: var(--white); }
  .back-brand {
    position: absolute; right: 26px; top: 28px;
    display: flex; flex-direction: column; align-items: center; gap: 10px;
  }
  .back-brand .brand-dot { width: 60px; height: 60px; background: var(--white); }
  .back-brand .brand-name { font-size: 22px; color: var(--white); }
  .taglines {
    position: absolute; left: 30px; top: 112px; right: 30px;
    list-style: none;
    display: flex; flex-direction: column; gap: 14px;
    font-size: 15px; letter-spacing: 0.8px; line-height: 1.2;
  }
  .taglines li:first-child { margin-right: 200px; }
  .back-web {
    position: absolute; left: 0; right: 0; bottom: 22px;
    text-align: center; font-size: 13px; letter-spacing: 0.6px;
  }
</style>
</head>
<body>

<section class="card card-front" aria-label="Business card front">
  <div class="side-band"><span class="side-band-name">Brambleton Gardenworks</span></div>

  <div class="front-brand">
    <span class="brand-dot"></span>
    <span class="brand-name">Brambleton Gardenworks</span>
  </div>

  <div class="person">
    <p class="person-name">Oliver Hartley</p>
    <p class="person-role">General Manager</p>
  </div>

  <ul class="contact-list">
    <li>
      <svg class="icon" viewBox="0 0 24 24"><path fill="#8dc63f" d="M6.6 10.8a15 15 0 0 0 6.6 6.6l2.2-2.2a1 1 0 0 1 1-.25 11.4 11.4 0 0 0 3.6.57 1 1 0 0 1 1 1V20a1 1 0 0 1-1 1A17 17 0 0 1 3 4a1 1 0 0 1 1-1h3.5a1 1 0 0 1 1 1c0 1.25.2 2.45.57 3.57a1 1 0 0 1-.25 1z"/></svg>
      +61 400 218 735
    </li>
    <li>
      <svg class="icon" viewBox="0 0 24 24"><path fill="#8dc63f" d="M12 2a7 7 0 0 0-7 7c0 5.25 7 13 7 13s7-7.75 7-13a7 7 0 0 0-7-7zm0 9.5A2.5 2.5 0 1 1 12 6.5a2.5 2.5 0 0 1 0 5z"/></svg>
      Street Name, City, Country
    </li>
    <li>
      <svg class="icon" viewBox="0 0 24 24"><rect x="2" y="5" width="20" height="14" rx="2" fill="#8dc63f"/><path d="M3 6l9 7 9-7" fill="none" stroke="#f7f7f7" stroke-width="1.6"/></svg>
      oliver.hartley@brambletongardenworks.com.au
    </li>
    <li>
      <svg class="icon" viewBox="0 0 24 24"><path fill="#8dc63f" d="M4 3l16 7-7 2-2 7z"/></svg>
      www.brambletongardenworks.com.au
    </li>
  </ul>

  <ul class="social-list">
    <li><span class="social-mark"></span>Brambleton Gardenworks</li>
    <li><span class="social-mark"></span>Brambleton Gardenworks</li>
    <li><span class="guild-badge" role="img" aria-label="The Turfcraft Guild badge"></span>The Turfcraft Guild Member</li>
    <li class="licence">Lic. 618392K</li>
  </ul>
</section>

<section class="card card-back" aria-label="Business card back">
  <div class="back-brand">
    <span class="brand-dot"></span>
    <span class="brand-name">Brambleton Gardenworks</span>
  </div>

  <ul class="taglines">
    <li>"Fully qualified, licensed &amp; insured"</li>
    <li>"Residential . Strata . Commercial . Real Estate"</li>
    <li>"Landscape Maintenance . Irrigation . Arboriculture"</li>
    <li>"Creating outdoor spaces for our community to be inspired, refreshed and re-energised"</li>
  </ul>

  <p class="back-web">www.brambletongardenworks.com.au</p>
</section>

</body>
</html>
```